SaaS Early tech startup business card design

Unique design for experience ecommerce platform company. the business cards will be used by executive members. conformance with color code is required.

```html
<!DOCTYPE html>
<html lang="en">
<head>
<meta charset="utf-8">
<title>Novira Business Card</title>
<link rel="stylesheet" href="https://fonts.googleapis.com/css2?family=Rubik:wght@500;700&family=Roboto:wght@400&display=swap">
<style>
  :root {
    --backdrop: #6b6566;
    --navy: #25263a;
    --navy-light: #3a3b52;
    --paper: #f3f3f4;
    --teal: #16a08f;
    --teal-deep: #0f6470;
    --ink: #2b2b2f;
    --white: #ffffff;
  }
  * { margin: 0; padding: 0; box-sizing: border-box; }
  html, body { width: 1200px; height: 1200px; overflow: hidden; }
  body { background: var(--backdrop); position: relative; font-family: "Roboto", sans-serif; }

  .card {
    position: absolute;
    width: 593px;
    height: 350px;
    border-radius: 26px;
    overflow: hidden;
  }
  .card--front { left: 300px; top: 198px; background: linear-gradient(115deg, var(--navy) 0%, var(--navy-light) 45%, var(--navy) 75%); }
  .card--back { left: 292px; top: 637px; background: var(--paper); }

  .wordmark {
    position: absolute;
    font-family: "Rubik", sans-serif;
    font-weight: 700;
    line-height: 1;
    letter-spacing: -1px;
    color: var(--teal);
  }
  .slogan {
    position: absolute;
    font-family: "Roboto", sans-serif;
    font-weight: 400;
    white-space: nowrap;
  }

  .card--front .wordmark { left: 57px; top: 122px; font-size: 84px; }
  .card--front .slogan { left: 60px; top: 203px; font-size: 17px; color: var(--white); }
  .card--front .line-art {
    position: absolute; right: 0; top: 0; width: 270px; height: 350px;
    background: radial-gradient(ellipse at 60% 45%, rgba(22,160,143,0.35), rgba(22,160,143,0.08) 65%, transparent 80%);
  }

  .accent-dot {
    position: absolute; left: -38px; top: 40px; width: 52px; height: 104px;
    border-radius: 50%; background: var(--teal);
  }
  .holder-name {
    position: absolute; left: 36px; top: 52px;
    font-family: "Rubik", sans-serif; font-weight: 500; font-size: 25px;
    color: var(--teal-deep); letter-spacing: -0.5px;
  }
  .holder-title { position: absolute; left: 37px; top: 88px; font-size: 15.5px; color: var(--ink); }

  .card--back .wordmark { left: 352px; top: 44px; font-size: 74px; color: var(--teal-deep); }
  .card--back .slogan { left: 357px; top: 117px; font-size: 15px; color: var(--teal); }

  .address { position: absolute; left: 37px; top: 190px; font-size: 15.5px; line-height: 22px; color: var(--ink); }
  .contacts { position: absolute; left: 37px; top: 246px; list-style: none; }
  .contacts li { display: flex; align-items: center; height: 22px; font-size: 15.5px; color: var(--ink); }
  .contacts svg { width: 14px; height: 14px; margin-right: 17px; fill: var(--teal-deep); }

  .card--back .line-art {
    position: absolute; left: 417px; top: 200px; width: 176px; height: 150px;
    background: radial-gradient(ellipse at 55% 55%, rgba(22,160,143,0.28), rgba(15,100,112,0.08) 60%, transparent 80%);
  }
</style>
</head>
<body>
  <section class="card card--front">
    <div class="line-art" role="img" aria-label="Decorative teal looping line pattern"></div>
    <div class="wordmark">novira</div>
    <div class="slogan">Built around you</div>
  </section>

  <section class="card card--back">
    <div class="accent-dot"></div>
    <div class="holder-name">Darin K.</div>
    <div class="holder-title">CTO/Owner</div>

    <div class="wordmark">novira</div>
    <div class="slogan">Built around you</div>

    <p class="address">Meridian House, Dubai<br>Harbor Tech Park, UAE</p>
    <ul class="contacts">
      <li>
        <svg viewBox="0 0 16 16" aria-hidden="true"><path d="M1 6c0-2 3-3 7-3s7 1 7 3v1h-3V5.5C11 5 9.5 4.8 8 4.8S5 5 4 5.5V7H1z"/><path d="M4 8l2-2h4l2 2v6H4z"/></svg>
        (00) 0111 NOVA
      </li>
      <li>
        <svg viewBox="0 0 16 16" aria-hidden="true"><path d="M1 3h14v10H1z M2.5 4.2L8 8.6l5.5-4.4z" fill-rule="evenodd"/></svg>
        info@novira.net
      </li>
      <li>
        <svg viewBox="0 0 16 16" aria-hidden="true"><path d="M8 1a7 7 0 100 14A7 7 0 008 1zm0 1.5c.8 0 1.7 1.6 2 4H6c.3-2.4 1.2-4 2-4zM2.6 6.5h2.3c0 .5-.1 1-.1 1.5s0 1 .1 1.5H2.6a5.6 5.6 0 010-3zm3.4 0h4c.1.5.1 1 .1 1.5s0 1-.1 1.5H6c-.1-.5-.1-1-.1-1.5s0-1 .1-1.5zm5.1 0h2.3a5.6 5.6 0 010 3h-2.3c.1-.5.1-1 .1-1.5s0-1-.1-1.5zM6 10.5h4c-.3 2.4-1.2 4-2 4s-1.7-1.6-2-4z"/></svg>
        www.novira.net
      </li>
    </ul>

    <div class="line-art" role="img" aria-label="Faint teal looping line pattern"></div>
  </section>
</body>
</html>
```